Business Card Design Project

I am an aviation professional (corporate pilot), and am looking to market myself to the business jet operators for short term crew leasing. The card should have name and contact info on the front side; qualifications, licenses held and type ratings on the back side.
Company name is: Harbinvale Skyline Partners Inc.
Updates

Sorry for the delay. will reply in another day or two.
best regards,

P

Target Market(s)

Business Jet Management companies and private jet operators

Industry/Entity Type

Business

Requirements
Must have
• It needs to be an aviation inspired design.

```html
<!DOCTYPE html>
<html lang="en">
<head>
<meta charset="utf-8">
<title>Business Card – Laurent Marvell</title>
<link rel="stylesheet" href="https://fonts.googleapis.com/css2?family=Ubuntu:wght@300;500&display=swap">
<style>
  :root {
    --page: #ffffff;
    --backdrop: #cbbd9e;
    --card: #432918;
    --edge: #6a5042;
    --text: #cdb19b;
    --heading: #d8bea8;
    --faint: #6d5244;
  }
  html, body {
    margin: 0;
    width: 1200px;
    height: 913px;
    overflow: hidden;
    background: var(--page);
  }
  .canvas {
    position: relative;
    width: 1200px;
    height: 913px;
    font-family: "Ubuntu", sans-serif;
    font-weight: 300;
  }
  .backdrop {
    position: absolute;
    left: 25px; top: 25px;
    width: 1150px; height: 862px;
    background: var(--backdrop);
  }
  .card {
    position: absolute;
    top: 200px;
    width: 309px;
    height: 513px;
    background: var(--card);
    border-left: 9px solid var(--edge);
    border-right: 9px solid var(--edge);
    box-sizing: border-box;
    color: var(--text);
    text-align: center;
    font-size: 19px;
    line-height: 21.6px;
  }
  .card--front { left: 272px; }
  .card--back { left: 619px; }
  .block {
    position: absolute;
    left: 0; right: 0;
    margin: 0;
  }
  .brand-mark {
    position: absolute;
    left: 106px; top: 30px;
    width: 78px; height: 78px;
    border-radius: 50%;
    background: var(--faint);
  }
  .brand-name {
    top: 168px;
    color: var(--faint);
    font-size: 21px;
    line-height: 23px;
  }
  .holder { top: 247px; }
  .holder .name, .section-title {
    font-weight: 500;
    color: var(--heading);
    display: block;
  }
  .address { top: 312px; font-style: normal; }
  .contacts { top: 420px; }
  .licenses { top: 183px; }
  .ratings { top: 247px; }
  .block span { display: block; }
</style>
</head>
<body>
<div class="canvas">
  <div class="backdrop"></div>

  <section class="card card--front">
    <div class="brand-mark"></div>
    <p class="block brand-name">Harbinvale Skyline<br>Partners Inc.</p>
    <p class="block holder"><span class="name">Laurent Marvell</span><span>Captain</span></p>
    <address class="block address">
      <span>57 Alder Ridge Road,</span>
      <span>Brantwood, ON,</span>
      <span>N3T4K8</span>
      <span>Canada</span>
    </address>
    <p class="block contacts">
      <span>+971 50 5550142 (M)</span>
      <span>+1 905 555 0187 (H)</span>
      <span>laurent.marvell@mailpost.com</span>
    </p>
  </section>

  <section class="card card--back">
    <p class="block licenses">
      <span class="section-title">Licenses</span>
      <span>NCAB &amp; Northern Air Board</span>
    </p>
    <p class="block ratings">
      <span class="section-title">Type Ratings</span>
      <span>Norvale Stratus 410/415</span>
      <span>Norvale SwiftJet 52XR</span>
      <span>Aerolon 810NX/BCJ</span>
      <span>Skyvane S240</span>
    </p>
  </section>
</div>
</body>
</html>
```